website re-design for: fern+lantern, complete vision care

we are a growing, cutting edge eye clinic with two locations in the palouse area of washington state, in the usa. we offer complete vision care, from spectacles and contacts to ocular disease management and treatment.

our current website was designed as a freebie, and was always meant to be a placeholder. we have reached a point where we would like our website to have a more stand-apart look and feel, while maintaining an intuitive user experience.

Target Market(s)

because our two clinics serve vastly different demographics, the website will have to speak to both. one clinic is located in a college town (majority of patients are 18-50 years+), while the other serves an older adult population (majority of patients 30-75 yrs+).

Industry/Entity Type

Health And Wellness

Logo Text

fern+lantern (including a logo lock-up version w/ "complete vision care")

Coding

Coded - Design and coding required

Number of Pages Required

5+ page

Font styles to use
Sans Serif
Other font styles liked:
• Verdana, and complementary fonts

Colors
606060
ffffff
33b8a4
86cfc6

Requirements
Must have
• - Pertinent contact information w/ Google maps
• - Clinic phone numbers at top of each page
• - An appointment request form
• - Page for Blog
• - Integrate with overall brand look and feel (e.g. Verdana font (we are open to complementary fonts), all lower case, except for prose,
• - Mobile friendly design
• - Code to maximize Search Engine Optimization (SEO)
Nice to have
• a design that speaks to the true nature of our business as an eye clinic, but feels different than typical eye care websites
Should not have
• this probably goes without saying, but the website should not have any political slant or otherwise bias

```html
<!DOCTYPE html>
<html lang="en">
<head>
<meta charset="utf-8">
<title>fern+lantern – Family Eye Care</title>
<meta name="viewport" content="width=1200">
<link href="https://fonts.googleapis.com/css2?family=Varela+Round&family=Open+Sans:ital,wght@0,400;0,600;0,700;1,400&display=swap" rel="stylesheet">
<style>
:root{
  --teal:#33b8a4;
  --teal-dark:#259a88;
  --teal-light:#86cfc6;
  --grey:#606060;
  --ink:#333333;
  --soft:#f3f3f3;
  --white:#ffffff;
  --line:#dcdcdc;
  --night:#2f3333;
}
*{box-sizing:border-box;margin:0;padding:0}
html,body{width:1200px;height:4286px;overflow:hidden}
body{position:relative;background:var(--white);font-family:"Open Sans",Verdana,sans-serif;color:var(--grey)}
.head{font-family:"Varela Round",Verdana,sans-serif}
.abs{position:absolute}
.section{position:absolute;left:0;width:1200px}
.title{position:absolute;left:0;width:1200px;text-align:center;font-family:"Varela Round",Verdana,sans-serif;font-size:38px;color:var(--teal);font-weight:700;letter-spacing:.5px}
.lede{position:absolute;left:240px;width:720px;text-align:center;font-size:14px;line-height:1.75;color:var(--grey)}
.btn{position:absolute;display:flex;height:54px;font-size:16px;font-weight:600;letter-spacing:.5px;text-transform:uppercase;color:var(--white)}
.btn .label{background:var(--teal);display:flex;align-items:center;padding:0 18px}
.btn .tip{background:var(--teal-light);width:40px;display:flex;align-items:center;justify-content:center}
/* header */
.brand-mark{left:77px;top:34px;width:60px;height:60px;background:#4d4d4d}
.brand-name{left:156px;top:30px;font-size:32px;color:var(--teal);font-weight:700}
.brand-tag{left:156px;top:74px;font-size:22px;color:#9fd6ce;letter-spacing:3px}
.social{width:44px;height:44px;border:2px solid #cfcfcf;border-radius:50%;top:44px}
.phone-pill{left:834px;top:42px;width:280px;height:52px;border:2px solid #d5d5d5;border-radius:26px;display:flex;align-items:center;gap:10px;padding-left:16px;font-size:18px;color:var(--ink);font-weight:600}
/* nav */
.nav{left:77px;top:134px;width:1043px;height:60px;background:var(--teal);display:flex;align-items:center}
.nav a{color:var(--white);text-decoration:none;font-size:14px;font-weight:600;text-transform:uppercase;padding:0 13px;height:60px;display:flex;align-items:center;border-right:1px solid rgba(255,255,255,.35)}
.nav a.active{background:var(--teal-dark)}
.search{margin-left:auto;margin-right:16px;width:190px;height:38px;background:#5cc7b7;border-radius:3px;display:flex;align-items:center;justify-content:space-between;padding:0 10px;color:#e8f7f4;font-size:14px}
/* hero */
.hero{top:194px;height:577px;background:linear-gradient(100deg,#ffffff 0%,#f4f4f4 45%,#ececec 100%)}
.hero-photo{left:560px;top:0;width:640px;height:577px;background:linear-gradient(120deg,#e9e9e9 0%,#d6c9bd 45%,#8f7866 70%,#e6e6e6 100%)}
.hero h1{position:absolute;left:77px;top:170px;width:560px;font-family:"Varela Round",Verdana,sans-serif;font-size:40px;line-height:1.25;color:var(--ink);font-weight:700}
.hero p{position:absolute;left:77px;top:280px;width:470px;font-size:17px;line-height:1.55;color:var(--ink)}
/* doctor */
.about{top:771px;height:860px;background:var(--soft)}
.doc-card{left:77px;top:366px;width:1043px;height:440px;border-radius:34px;background:linear-gradient(180deg,var(--teal) 0%,#5cc4b5 60%,var(--teal-light) 100%)}
.doc-photo{left:36px;top:70px;width:286px;height:286px;border-radius:50%;border:10px solid var(--white);background:linear-gradient(160deg,#f2f2f2 0%,#d8d2cc 60%,#b9c3c9 100%)}
.doc-card h3{position:absolute;left:403px;top:58px;font-family:"Varela Round",Verdana,sans-serif;font-size:30px;color:var(--white)}
.doc-name{left:403px;top:114px;font-size:19px;color:var(--white);font-weight:600}
.doc-role{left:403px;top:140px;font-size:13px;color:var(--white);font-style:italic;font-weight:700}
.doc-card p.copy{position:absolute;left:403px;width:600px;font-size:13.5px;line-height:1.7;color:var(--white)}
.doc-more{left:403px;top:340px;font-size:15px;color:var(--white);text-decoration:underline;letter-spacing:.5px;display:flex;align-items:center;gap:8px}
/* services */
.services{top:1631px;height:663px}
.svc{position:absolute;top:163px;width:250px;height:314px;background:var(--teal-light)}
.svc-photo{position:absolute;left:8px;top:8px;width:234px;height:162px}
.svc h4{position:absolute;left:0;top:190px;width:250px;text-align:center;color:var(--white);font-size:18px;line-height:1.35;font-weight:600}
.svc-icon{position:absolute;left:83px;top:248px;width:84px;height:84px;border-radius:50%;background:var(--white);border:2px solid #e2e2e2;display:flex;align-items:center;justify-content:center}
.svc-nav{position:absolute;top:305px;width:44px;height:44px;border-radius:50%;display:flex;align-items:center;justify-content:center}
/* clinic */
.clinic{top:2294px;height:549px;background:linear-gradient(180deg,var(--teal) 0%,#3cbda9 100%)}
.clinic .title,.clinic .lede{color:var(--white)}
.step{position:absolute;display:flex;align-items:center;justify-content:center;border-radius:50%}
.step-label{position:absolute;top:372px;width:200px;text-align:center;color:var(--white);font-size:15px;font-weight:600}
/* blog */
.blog{top:2843px;height:628px}
.post{position:absolute;top:151px;width:337px;height:414px;background:#f6f6f6}
.post.featured{background:var(--teal)}
.post-photo{position:absolute;left:8px;top:8px;width:321px;height:206px}
.post h5{position:absolute;left:8px;top:250px;width:321px;font-size:18px;color:var(--teal);font-weight:700}
.post.featured h5,.post.featured .meta,.post.featured p{color:var(--white)}
.post .meta{position:absolute;left:8px;right:8px;top:294px;display:flex;justify-content:space-between;font-size:12px;color:#8a8a8a;font-style:italic;padding-bottom:12px;border-bottom:1px solid rgba(0,0,0,.1)}
.post p{position:absolute;left:8px;top:335px;width:310px;font-size:13px;line-height:1.7;color:var(--grey)}
.post p u{font-weight:700}
/* hours */
.hours{top:3471px;height:729px;background:linear-gradient(180deg,var(--teal) 0%,var(--teal) 66%,#3a3d3d 66%,#262828 100%)}
.hours .title{color:var(--white);top:78px}
.loc{position:absolute;top:135px;width:294px;height:508px;background:var(--white);padding:28px 20px}
.loc h6{font-size:17px;color:var(--ink);font-weight:700;margin-bottom:14px}
.loc .row{display:flex;gap:10px;font-size:12.5px;line-height:1.5;color:var(--grey);margin-bottom:9px}
.loc .row svg{flex:0 0 16px;margin-top:2px}
.loc .link{color:var(--teal);text-decoration:underline}
.loc .rule{border-top:1px solid var(--line);margin:8px 0 12px}
.loc-map{position:absolute;left:16px;bottom:14px;width:262px;height:80px;background:linear-gradient(135deg,#e6ece4 0%,#d7e3ee 55%,#eef0ea 100%)}
.appt{position:absolute;left:731px;top:135px;width:389px;height:508px;background:var(--white);padding:30px 24px}
.appt h6{font-family:"Varela Round",Verdana,sans-serif;font-size:28px;color:var(--teal);text-align:center;font-weight:700}
.appt .sub{text-align:center;font-style:italic;font-size:15px;color:var(--grey);margin:12px 0 18px;padding-bottom:18px;border-bottom:1px solid var(--line)}
.field{display:flex;height:50px;margin-bottom:12px;background:#f0f0f0}
.field .ico{width:50px;background:var(--teal);display:flex;align-items:center;justify-content:center}
.field .ph{flex:1;display:flex;align-items:center;justify-content:space-between;padding:0 14px;font-size:14px;font-style:italic;color:#777}
.submit{height:52px;background:var(--teal);color:var(--white);font-size:17px;font-weight:700;display:flex;align-items:center;justify-content:center;text-transform:uppercase;letter-spacing:.5px}
/* footer */
.footer{top:4200px;height:86px;background:var(--night);display:flex;align-items:center;padding:0 77px;color:#e8e8e8;font-size:14px}
.footer .sep{margin:0 8px;color:#999}
.footer .fsocial{width:44px;height:44px;border-radius:50%;background:#4a4e4e;margin-left:12px}
</style>
</head>
<body>

<!-- header -->
<header>
  <div class="abs brand-mark" aria-hidden="true"></div>
  <div class="abs brand-name head">fern+lantern</div>
  <div class="abs brand-tag head">Family Eye Care</div>
  <span class="abs social" style="left:600px" aria-label="social link"></span>
  <span class="abs social" style="left:652px" aria-label="social link"></span>
  <span class="abs social" style="left:704px" aria-label="social link"></span>
  <span class="abs social" style="left:756px" aria-label="social link"></span>
  <div class="abs phone-pill">
    <svg width="20" height="20" viewBox="0 0 24 24"><path d="M6.6 10.8a15.1 15.1 0 0 0 6.6 6.6l2.2-2.2a1 1 0 0 1 1-.25 11.4 11.4 0 0 0 3.6.6 1 1 0 0 1 1 1V20a1 1 0 0 1-1 1A17 17 0 0 1 3 4a1 1 0 0 1 1-1h3.5a1 1 0 0 1 1 1c0 1.25.2 2.45.6 3.6a1 1 0 0 1-.25 1z" fill="#606060"/></svg>
    509-555-0142,&nbsp; 509-555-0187
  </div>
  <nav class="abs nav">
    <a class="active">Home</a>
    <a>Hours &amp; Locations</a>
    <a>Our Eye Doctor</a>
    <a>Our Eye Care Clinic</a>
    <a>Eye Care Services</a>
    <a style="border-right:none">Insurance</a>
    <div class="search">Search...
      <svg width="16" height="16" viewBox="0 0 24 24"><circle cx="10" cy="10" r="6.5" fill="none" stroke="#fff" stroke-width="2.5"/><path d="M15 15l6 6" stroke="#fff" stroke-width="2.5"/></svg>
    </div>
  </nav>
</header>

<!-- hero -->
<section class="section hero">
  <div class="abs hero-photo" role="img" aria-label="Photo of an optometrist fitting trial frames on a smiling patient"></div>
  <h1>Helping People Gain Power<br>their Eyes</h1>
  <p>Lorem Ipsum is simply dummy text of the printing and typesetting industry. Lorem Ipsum has been the industry's standard dummy text ever since the 1500s</p>
  <div class="btn" style="left:77px;top:377px"><span class="label">Contact Us</span><span class="tip"><svg width="14" height="16" viewBox="0 0 14 16"><path d="M3 2l7 6-7 6" fill="none" stroke="#fff" stroke-width="3"/></svg></span></div>
</section>

<!-- our eye doctor -->
<section class="section about">
  <h2 class="title" style="top:52px">OUR EYE DOCTOR</h2>
  <p class="lede" style="top:115px">Eye care professionals specialize in understanding how the human eye really works, as well as diseases and conditions that affect your vision – many of which do not have obvious symptoms. Eye doctors know how age and risk factors affect vision over time for young and old, and they understand the benefits and features of corrective lenses including eyeglasses and contacts.</p>
  <div class="btn" style="left:512px;top:238px"><span class="label">Read More</span><span class="tip"><svg width="14" height="16" viewBox="0 0 14 16"><path d="M3 2l7 6-7 6" fill="none" stroke="#fff" stroke-width="3"/></svg></span></div>

  <div class="abs doc-card">
    <div class="abs doc-photo" role="img" aria-label="Portrait photo of Dr. Owen Hartley in a white coat"></div>
    <svg class="abs" style="left:20px;top:50px" width="340" height="340" viewBox="0 0 340 340">
      <defs><path id="docArc" d="M200 22 A150 150 0 0 1 250 300"/></defs>
      <text font-family="Varela Round, Verdana, sans-serif" font-size="22" fill="#fff" letter-spacing="1.5"><textPath href="#docArc">Dr.-Owen-Hartley</textPath></text>
    </svg>
    <h3>Meet our doctor</h3>
    <div class="abs doc-name">Dr. Owen Hartley</div>
    <div class="abs doc-role">Clinical Director</div>
    <p class="copy" style="top:180px">Owen Hartley completed the Doctor of Optometry program at Bayview College of Optometry in May 2016.</p>
    <p class="copy" style="top:240px">He opted to become residency trained, with a focus on ocular disease, at Riverside Veterans Medical Center in Spokane, Washington. Owen also completed internships at sites renowned for their focus on ocular disease.</p>
    <div class="abs doc-more">READ MORE <svg width="10" height="12" viewBox="0 0 10 12"><path d="M2 1l5 5-5 5" fill="none" stroke="#fff" stroke-width="2.2"/></svg></div>
  </div>
</section>

<!-- eye care services -->
<section class="section services">
  <h2 class="title" style="top:2px">EYE CARE SERVICES</h2>
  <p class="lede" style="top:62px">The full spectrum of eye care is offered to clients of all ages, from children to older adults: vision tests, corrective laser eye surgery, immediate attention for eye emergencies and so much more.</p>

  <div class="svc-nav" style="left:21px;background:var(--teal)"><svg width="12" height="16" viewBox="0 0 12 16"><path d="M9 2L3 8l6 6" fill="none" stroke="#fff" stroke-width="3"/></svg></div>
  <div class="svc-nav" style="left:1135px;background:#d0d0d0"><svg width="12" height="16" viewBox="0 0 12 16"><path d="M3 2l6 6-6 6" fill="none" stroke="#555" stroke-width="3"/></svg></div>

  <div class="svc" style="left:77px">
    <div class="svc-photo" role="img" aria-label="Photo of a patient at a slit lamp during an eye exam" style="background:linear-gradient(135deg,#9bb0b8,#3f5860)"></div>
    <h4>Comprehensive Eye<br>Exams</h4>
    <div class="svc-icon"><svg width="44" height="24" viewBox="0 0 44 24"><circle cx="11" cy="14" r="8" fill="none" stroke="#555" stroke-width="2.5"/><circle cx="33" cy="14" r="8" fill="none" stroke="#555" stroke-width="2.5"/><path d="M19 12q3-3 6 0M3 12L1 5M41 12l2-7" fill="none" stroke="#555" stroke-width="2.5"/></svg></div>
  </div>
  <div class="svc" style="left:343px">
    <div class="svc-photo" role="img" aria-label="Photo of a woman trying on eyeglasses" style="background:linear-gradient(135deg,#d9c7b8,#8c6e5e)"></div>
    <h4>Presbyopia Diagnosis<br>and Treatment</h4>
    <div class="svc-icon"><svg width="40" height="30" viewBox="0 0 40 30"><path d="M2 15Q20-3 38 15Q20 33 2 15z" fill="none" stroke="#555" stroke-width="2.5"/><circle cx="20" cy="15" r="5" fill="#555"/></svg></div>
  </div>
  <div class="svc" style="left:609px">
    <div class="svc-photo" role="img" aria-label="Close-up photo of eye drops being applied" style="background:linear-gradient(135deg,#e8d5c8,#a9887a)"></div>
    <h4>Dry Eye Disease and<br>Treatment</h4>
    <div class="svc-icon"><svg width="40" height="30" viewBox="0 0 40 30"><path d="M2 15Q20-3 38 15Q20 33 2 15z" fill="none" stroke="#555" stroke-width="2.5"/><circle cx="20" cy="15" r="7" fill="none" stroke="#555" stroke-width="2.5"/><circle cx="20" cy="15" r="3" fill="#555"/></svg></div>
  </div>
  <div class="svc" style="left:872px">
    <div class="svc-photo" role="img" aria-label="Photo of a child at an eye testing instrument" style="background:linear-gradient(135deg,#f1e4dd,#b9a8a0)"></div>
    <h4>Pediatric<br>Eye Exams</h4>
    <div class="svc-icon"><svg width="36" height="36" viewBox="0 0 36 36"><circle cx="12" cy="9" r="5" fill="#555"/><path d="M5 34V19q7-4 14 0v15z" fill="#555"/><rect x="22" y="12" width="11" height="14" fill="none" stroke="#555" stroke-width="2.2"/></svg></div>
  </div>

  <div class="btn" style="left:512px;top:549px"><span class="label">View All</span><span class="tip"><svg width="14" height="16" viewBox="0 0 14 16"><path d="M3 2l7 6-7 6" fill="none" stroke="#fff" stroke-width="3"/></svg></span></div>
</section>

<!-- our eye care clinic -->
<section class="section clinic">
  <h2 class="title" style="top:58px">OUR EYE CARE CLINIC</h2>
  <p class="lede" style="top:122px">Welcome to our online Practice! Our eye doctor and eye care staff are here to care for all of your vision needs. We handle everything from adult and children's eye exams and hard-to-fit contact lenses, to eye emergencies, treatment of eye diseases and co-management of eye surgery such as LASIK.</p>
  <svg class="abs" style="left:330px;top:290px" width="540" height="20"><line x1="0" y1="10" x2="540" y2="10" stroke="#fff" stroke-width="3"/></svg>
  <div class="step" style="left:392px;top:258px;width:84px;height:84px;background:#fff"><div class="step" style="position:static;width:64px;height:64px;background:var(--teal-dark)"><svg width="36" height="26" viewBox="0 0 40 30"><path d="M2 15Q20-3 38 15Q20 33 2 15z" fill="none" stroke="#fff" stroke-width="3"/><circle cx="20" cy="15" r="6" fill="#fff"/></svg></div></div>
  <div class="step" style="left:552px;top:252px;width:96px;height:96px;background:#fff;border:4px solid #cde9e4"><svg width="40" height="40" viewBox="0 0 40 40"><circle cx="20" cy="12" r="7" fill="#555"/><path d="M6 38q2-14 14-14t14 14z" fill="#555"/><rect x="24" y="4" width="12" height="9" rx="2" fill="var(--teal)"/></svg></div>
  <div class="step" style="left:724px;top:258px;width:84px;height:84px;background:#fff"><div class="step" style="position:static;width:64px;height:64px;background:var(--teal-dark)"><svg width="32" height="32" viewBox="0 0 32 32"><circle cx="16" cy="16" r="9" fill="none" stroke="#fff" stroke-width="4" stroke-dasharray="5 3"/><circle cx="16" cy="16" r="4" fill="#fff"/></svg></div></div>
  <div class="step-label" style="left:334px">Great Vision</div>
  <div class="step-label" style="left:500px">Advice</div>
  <div class="step-label" style="left:666px">Technology and Fit</div>
  <div class="btn" style="left:515px;top:426px;color:var(--ink)"><span class="label" style="background:#fff">Read More</span><span class="tip" style="background:var(--ink)"><svg width="14" height="16" viewBox="0 0 14 16"><path d="M3 2l7 6-7 6" fill="none" stroke="#fff" stroke-width="3"/></svg></span></div>
</section>

<!-- blog -->
<section class="section blog">
  <h2 class="title" style="top:62px">OUR RECENT BLOG POST</h2>
  <article class="post featured" style="left:77px">
    <div class="post-photo" role="img" aria-label="Photo of a smiling older couple embracing outdoors" style="background:linear-gradient(135deg,#b8cf9c,#6f8f55)"></div>
    <h5>Lorem Ipsum typesetting industry.</h5>
    <div class="meta"><span>16 June 2018</span><span>&#9673; 56 &nbsp; &#9825; 0</span></div>
    <p>Lorem Ipsum is simply dummy text of the printing and typesetting industry. <u>READ MORE</u></p>
  </article>
  <article class="post" style="left:437px">
    <div class="post-photo" role="img" aria-label="Photo of a receptionist working at a computer in an optical store" style="background:linear-gradient(135deg,#f2f2f2,#c9c1bb)"></div>
    <h5>Lorem Ipsum typesetting industry.</h5>
    <div class="meta"><span>16 June 2018</span><span>&#9673; 56 &nbsp; &#9825; 0</span></div>
    <p>Lorem Ipsum is simply dummy text of the printing and typesetting industry. <u style="color:var(--teal)">READ MORE</u></p>
  </article>
  <article class="post" style="left:794px">
    <div class="post-photo" role="img" aria-label="Photo of a smiling girl wearing glasses" style="background:linear-gradient(135deg,#f5e7df,#c9a896)"></div>
    <h5>Lorem Ipsum typesetting industry.</h5>
    <div class="meta"><span>16 June 2018</span><span>&#9673; 56 &nbsp; &#9825; 0</span></div>
    <p>Lorem Ipsum is simply dummy text of the printing and typesetting industry. <u style="color:var(--teal)">READ MORE</u></p>
  </article>
</section>

<!-- hours & locations -->
<section class="section hours">
  <div class="abs" role="img" aria-label="Faded photo collage of clinic patients behind the location cards" style="left:0;top:481px;width:1200px;height:248px"></div>
  <h2 class="title">HOURS &amp; LOCATIONS</h2>

  <div class="loc" style="left:77px">
    <h6>Pullman Location</h6>
    <div class="row"><svg width="16" height="16" viewBox="0 0 24 24"><path d="M12 2a7 7 0 0 0-7 7c0 5 7 13 7 13s7-8 7-13a7 7 0 0 0-7-7zm0 9.5A2.5 2.5 0 1 1 12 6.5a2.5 2.5 0 0 1 0 5z" fill="var(--teal)"/></svg><div><span class="link">Northgate Vision Center</span><br>1420 SE Meadow Lane<br>Pullman, WA 99163</div></div>
    <div class="rule"></div>
    <div class="row"><svg width="16" height="16" viewBox="0 0 24 24"><path d="M6.6 10.8a15.1 15.1 0 0 0 6.6 6.6l2.2-2.2a1 1 0 0 1 1-.25 11.4 11.4 0 0 0 3.6.6 1 1 0 0 1 1 1V20a1 1 0 0 1-1 1A17 17 0 0 1 3 4a1 1 0 0 1 1-1h3.5a1 1 0 0 1 1 1c0 1.25.2 2.45.6 3.6a1 1 0 0 1-.25 1z" fill="var(--ink)"/></svg>509-555-0142</div>
    <div class="row"><svg width="16" height="16" viewBox="0 0 24 24"><rect x="3" y="8" width="18" height="12" fill="var(--ink)"/><rect x="7" y="3" width="10" height="6" fill="none" stroke="var(--ink)" stroke-width="2"/></svg>509-555-0149</div>
    <div class="row"><svg width="16" height="16" viewBox="0 0 24 24"><rect x="2" y="5" width="20" height="14" fill="none" stroke="var(--ink)" stroke-width="2"/><path d="M2 5l10 8 10-8" fill="none" stroke="var(--ink)" stroke-width="2"/></svg>contact@fernlanternwa.com</div>
    <div class="rule"></div>
    <div class="row"><svg width="16" height="16" viewBox="0 0 24 24"><circle cx="12" cy="12" r="9" fill="none" stroke="var(--ink)" stroke-width="2"/><path d="M12 7v5l3 2" fill="none" stroke="var(--ink)" stroke-width="2"/></svg><div><b><i>Tuesday :</i></b> 9:00 AM - 5:00 PM</div></div>
    <div class="row"><svg width="16" height="16" viewBox="0 0 24 24"><circle cx="12" cy="12" r="9" fill="none" stroke="var(--ink)" stroke-width="2"/><path d="M12 7v5l3 2" fill="none" stroke="var(--ink)" stroke-width="2"/></svg><div><b><i>Saturday :</i></b> 9:00 AM - 5:00 PM</div></div>
    <div class="loc-map" role="img" aria-label="Map showing the Pullman clinic location"></div>
  </div>

  <div class="loc" style="left:403px">
    <h6>Clarkston Location</h6>
    <div class="row"><svg width="16" height="16" viewBox="0 0 24 24"><path d="M12 2a7 7 0 0 0-7 7c0 5 7 13 7 13s7-8 7-13a7 7 0 0 0-7-7zm0 9.5A2.5 2.5 0 1 1 12 6.5a2.5 2.5 0 0 1 0 5z" fill="var(--teal)"/></svg><div><span class="link">Northgate Vision Center</span><br>218 Birch Street<br>Clarkston, WA 99403</div></div>
    <div class="rule"></div>
    <div class="row"><svg width="16" height="16" viewBox="0 0 24 24"><path d="M6.6 10.8a15.1 15.1 0 0 0 6.6 6.6l2.2-2.2a1 1 0 0 1 1-.25 11.4 11.4 0 0 0 3.6.6 1 1 0 0 1 1 1V20a1 1 0 0 1-1 1A17 17 0 0 1 3 4a1 1 0 0 1 1-1h3.5a1 1 0 0 1 1 1c0 1.25.2 2.45.6 3.6a1 1 0 0 1-.25 1z" fill="var(--ink)"/></svg>509-555-0187</div>
    <div class="row"><svg width="16" height="16" viewBox="0 0 24 24"><rect x="3" y="8" width="18" height="12" fill="var(--ink)"/><rect x="7" y="3" width="10" height="6" fill="none" stroke="var(--ink)" stroke-width="2"/></svg>509-555-0193</div>
    <div class="row"><svg width="16" height="16" viewBox="0 0 24 24"><rect x="2" y="5" width="20" height="14" fill="none" stroke="var(--ink)" stroke-width="2"/><path d="M2 5l10 8 10-8" fill="none" stroke="var(--ink)" stroke-width="2"/></svg>contact@fernlanternwa.com</div>
    <div class="rule"></div>
    <div class="row"><svg width="16" height="16" viewBox="0 0 24 24"><circle cx="12" cy="12" r="9" fill="none" stroke="var(--ink)" stroke-width="2"/><path d="M12 7v5l3 2" fill="none" stroke="var(--ink)" stroke-width="2"/></svg><div><b><i>Wednesday :</i></b> 9:00 AM - 5:00 PM</div></div>
    <div class="row"><svg width="16" height="16" viewBox="0 0 24 24"><circle cx="12" cy="12" r="9" fill="none" stroke="var(--ink)" stroke-width="2"/><path d="M12 7v5l3 2" fill="none" stroke="var(--ink)" stroke-width="2"/></svg><div><b><i>Thursday :</i></b> 9:00 AM - 5:00 PM</div></div>
    <div class="row"><svg width="16" height="16" viewBox="0 0 24 24"><circle cx="12" cy="12" r="9" fill="none" stroke="var(--ink)" stroke-width="2"/><path d="M12 7v5l3 2" fill="none" stroke="var(--ink)" stroke-width="2"/></svg><div><b><i>Friday :</i></b> 9:00 AM - 5:00 PM</div></div>
    <div class="loc-map" role="img" aria-label="Map showing the Clarkston clinic location"></div>
  </div>

  <form class="appt">
    <h6>Book an Appointments</h6>
    <div class="sub">Walking is People 's best Checkup</div>
    <div class="field"><span class="ico"><svg width="20" height="20" viewBox="0 0 24 24"><circle cx="12" cy="8" r="5" fill="#fff"/><path d="M3 22q1-9 9-9t9 9z" fill="#fff"/></svg></span><span class="ph">Name :</span></div>
    <div class="field"><span class="ico"><svg width="20" height="20" viewBox="0 0 24 24"><rect x="2" y="5" width="20" height="14" fill="none" stroke="#fff" stroke-width="2"/><path d="M2 5l10 8 10-8" fill="none" stroke="#fff" stroke-width="2"/></svg></span><span class="ph">Email :</span></div>
    <div class="field"><span class="ico"><svg width="20" height="20" viewBox="0 0 24 24"><path d="M6.6 10.8a15.1 15.1 0 0 0 6.6 6.6l2.2-2.2a1 1 0 0 1 1-.25 11.4 11.4 0 0 0 3.6.6 1 1 0 0 1 1 1V20a1 1 0 0 1-1 1A17 17 0 0 1 3 4a1 1 0 0 1 1-1h3.5a1 1 0 0 1 1 1c0 1.25.2 2.45.6 3.6a1 1 0 0 1-.25 1z" fill="#fff"/></svg></span><span class="ph">Phone :</span></div>
    <div class="field"><span class="ico"><svg width="20" height="20" viewBox="0 0 24 24"><rect x="2" y="6" width="20" height="14" rx="2" fill="#fff"/><circle cx="12" cy="13" r="4" fill="var(--teal)"/></svg></span><span class="ph">Department : <svg width="12" height="8" viewBox="0 0 12 8"><path d="M1 1l5 5 5-5" fill="none" stroke="#777" stroke-width="2"/></svg></span></div>
    <div class="submit">Submit Now</div>
  </form>
</section>

<!-- footer -->
<footer class="section footer">
  <span>Powered by ClinicSites.net<span class="sep">|</span>Email Accessibility<span class="sep">|</span>Website Accessibility Policy<span class="sep">|</span>Login</span>
  <span style="margin-left:auto;display:flex">
    <span class="fsocial" aria-label="social link"></span>
    <span class="fsocial" aria-label="social link"></span>
    <span class="fsocial" aria-label="social link"></span>
    <span class="fsocial" aria-label="social link"></span>
  </span>
</footer>

</body>
</html>
```